Business Card Design for Consulting Company

I require a Business Card design for my Consulting company. <br/><br/>My company name is: Marek Olvani Consulting Inc.<br/>My website is: www.marekolvaniconsulting.example<br/><br/>My company focuses on management and software development for the Tallobrix CRM platform (www.tallobrix.example)<br/><br/>I have a logo already designed...see attached.
Updates

Also Include my Name and Title: Marek T.L. Olvani President

Target Market(s)

Tallobrix Customers

Contact Information for Business Card

Only include my LOGO (provided)
My Name: Marek TL Olvani
My Title: President
My Company Name: Marek Olvani Consulting Inc.
My Website: www.marekolvaniconsulting.example
My Email: marek.olvani.consulting@mailbox.example

NO PHONE NUMBER
NO ADDRESS

Font styles to use
Serif
Sans Serif
Other font styles liked:
• see my website: www.marekolvaniconsulting.example

Colors

Designer to choose colors to be used in the design.

Requirements
Must have
• Must include my Orange
• Include my name (Marek T.L. Olvani), title (President) company name, website and email
• It should also have a tag line like: Tallobrix Consulting
• I'm flexible with the tag line
Should not have
• Don't include my phone number or address

```html
<!DOCTYPE html>
<html lang="en">
<head>
<meta charset="utf-8">
<title>Marek Olvani Consulting Inc. — Business Card</title>
<link rel="stylesheet" href="https://fonts.googleapis.com/css2?family=Michroma&family=Arimo:wght@400;700&display=swap">
<style>
  :root {
    --backdrop: #2b2b2c;
    --card-white: #ffffff;
    --card-dark: #1f2022;
    --brand-orange: #f5820f;
    --ink: #1c1c1c;
    --ink-soft: #555555;
    --tag-white: #e9e9e9;
  }
  * { margin: 0; padding: 0; box-sizing: border-box; }
  html, body {
    width: 1200px; height: 1108px; overflow: hidden;
    background: var(--backdrop);
  }
  .stage {
    position: relative; width: 1200px; height: 1108px;
    display: flex; justify-content: center; align-items: center; gap: 60px;
  }
  .card {
    position: relative; width: 380px; height: 668px;
    border-radius: 24px; overflow: hidden;
  }
  .card--front { background: var(--card-white); }
  .card--back { background: var(--card-dark); }

  .brand {
    position: absolute; left: 0; right: 0; top: 150px;
    display: flex; justify-content: center; align-items: center; gap: 12px;
  }
  .brand__square {
    width: 22px; height: 22px; background: var(--brand-orange); flex: none;
  }
  .brand__name {
    font-family: "Michroma", sans-serif; font-size: 14px;
    color: var(--brand-orange); letter-spacing: 0.5px; line-height: 1.5;
    text-transform: uppercase;
  }

  .holder {
    position: absolute; left: 34px; right: 24px; top: 430px;
  }
  .holder__name {
    font-family: "Michroma", sans-serif; font-weight: 400; font-size: 20px;
    color: var(--brand-orange); letter-spacing: 1px;
    text-transform: uppercase; white-space: nowrap;
  }
  .holder__title {
    font-family: "Arimo", sans-serif; font-size: 14px;
    color: var(--ink-soft); letter-spacing: 2px; text-transform: uppercase;
    margin: 8px 0 22px;
  }
  .holder__contact {
    font-family: "Arimo", sans-serif; font-size: 15.5px;
    color: var(--ink); line-height: 1.75; list-style: none;
    white-space: nowrap;
  }

  .back-mark {
    position: absolute; right: 50px; top: 420px;
    display: flex; align-items: center; gap: 8px;
  }
  .back-mark__square { width: 14px; height: 14px; background: var(--brand-orange); }
  .back-mark__name {
    font-family: "Michroma", sans-serif; font-size: 13px;
    color: var(--brand-orange); text-transform: uppercase;
  }
  .tagline {
    position: absolute; left: 0; right: 0; bottom: 96px; text-align: center;
    font-family: "Arimo", sans-serif; font-weight: 700; font-size: 18px;
    color: var(--tag-white); letter-spacing: 1px; text-transform: uppercase;
  }
</style>
</head>
<body>
<main class="stage">
  <section class="card card--front" aria-label="Card front">
    <div class="brand">
      <span class="brand__square"></span>
      <span class="brand__name">Marek Olvani<br>Consulting Inc.</span>
    </div>
    <div class="holder">
      <h1 class="holder__name">Marek T.L. Olvani</h1>
      <p class="holder__title">President</p>
      <ul class="holder__contact">
        <li>marek.olvani.consulting@mailbox.example</li>
        <li>www.marekolvaniconsulting.example</li>
      </ul>
    </div>
  </section>

  <section class="card card--back" aria-label="Card back">
    <div class="back-mark">
      <span class="back-mark__square"></span>
      <span class="back-mark__name">Marek Olvani</span>
    </div>
    <p class="tagline">Tallobrix Consulting</p>
  </section>
</main>
</body>
</html>
```